Varga Lillas Physiotherapy Business Card Vienna

We need a business card design for a newly created Physiotherapy company based in Vienna Austria.
We seek a simple, modern, minimalist design without too much color variation. The font should look young/fresh, but definitely not childish or so. Since we are a starting Business, we currently haven't got a logo, if you feel like a logo would fit your design, feel free to use one, but it's not necessary.
Target Market(s)
Healthcare, young and elderly people with mobility issues
Industry/Entity Type
Health And Wellness
Contact Information for Business Card
Name: Lilla Varga
Title description: Physiotherapist
Phone num: +43 664 5290 4816
e-mail: lilla.praxis@brelomail.com
Colors
Designer to choose colors to be used in the design.
Requirements
Must have
- Final design language must be in German, basically, the Title Description needs to be "Physiotherapeutin" the other details remain as in the English Language.
Nice to have
- Simple, modern, minimalist design
Should not have
- too many colors, Obvious use of a skeleton, skull, spline

```html
<!DOCTYPE html>
<html lang="de">
<head>
<meta charset="utf-8">
<title>Lilla Varga – Physiotherapie Visitenkarte</title>
<link rel="stylesheet" href="https://fonts.googleapis.com/css2?family=Poppins:wght@400;600;800&display=swap">
<style>
  :root {
    --backdrop: #000000;
    --card: #dcd1c0;
    --teal: #1a9a8f;
    --ink: #111111;
  }
  * { margin: 0; padding: 0; box-sizing: border-box; }
  html, body {
    width: 1200px;
    height: 800px;
    overflow: hidden;
    background: var(--backdrop);
  }
  .canvas {
    position: relative;
    width: 1200px;
    height: 800px;
  }
  .business-card {
    position: absolute;
    left: 187px;
    top: 132px;
    width: 826px;
    height: 535px;
    background: var(--card);
  }
  .practice-title {
    position: absolute;
    left: 59px;
    top: 52px;
    font-family: "Poppins", sans-serif;
    font-weight: 800;
    font-size: 75px;
    line-height: 65px;
    color: var(--teal);
    letter-spacing: 0.5px;
  }
  .accent-dash {
    position: absolute;
    left: 59px;
    top: 333px;
    width: 30px;
    height: 4px;
    background: var(--teal);
  }
  .contact {
    position: absolute;
    left: 57px;
    top: 351px;
    font-family: "Poppins", sans-serif;
    color: var(--ink);
  }
  .contact-name {
    font-weight: 600;
    font-size: 29px;
    line-height: 33px;
    margin-bottom: 2px;
  }
  .contact-line {
    font-weight: 400;
    font-size: 24px;
    line-height: 33px;
  }
</style>
</head>
<body>
  <main class="canvas">
    <section class="business-card">
      <h1 class="practice-title">PHYSIO<br>THERAPIE</h1>
      <div class="accent-dash"></div>
      <div class="contact">
        <p class="contact-name">Lilla Varga</p>
        <p class="contact-line">Physiotherapeutin</p>
        <p class="contact-line">P: +43 664 5290 4816</p>
        <p class="contact-line">E: lilla.praxis@brelomail.com</p>
      </div>
    </section>
  </main>
</body>
</html>
```